Hip Music Management Co. BIz Card

I have a logo (attached) the back side of the card should the full logo on the entire card- that's it. The front side of the card should show the logo somewhere, keeping with the 4 different shades of blue. The front side of the card can be a white background with logo and colored typeface for all info. Pretty simple.

Target Market(s)

I manage and produce a whole bunch of major label and indie artists.

Industry/Entity Type

Management

Contact Information for Business Card

Velmora Sound House (logo)
Dale Fornwick
President
www.velmorasoundhouse.com
dale@velmorasoundhouse.com
+1 310.555.7182
418 Willow Bend Lane
Ashgrove Falls, NY 10599

Requirements
Must have
• Entire logo on back side. White background on front- unless you provide something more interesting.
Nice to have
• On the front of the card if you choose a white backgound, if possible take my logo without the blue background (over white) that would be cool.

```html
<!DOCTYPE html>
<html lang="en">
<head>
<meta charset="utf-8">
<title>Velmora Sound House — Business Card</title>
<link rel="stylesheet" href="https://fonts.googleapis.com/css2?family=Lato:wght@400;700;900&display=swap">
<style>
  :root {
    --backdrop: #e9e6e1;
    --navy: #17214a;
    --teal: #1bb1be;
    --sky: #6cc9ec;
    --azure: #1a7bbf;
    --paper: #ffffff;
    --ink: #4a4a4a;
  }
  * { box-sizing: border-box; margin: 0; padding: 0; }
  html, body {
    width: 1200px; height: 1023px; overflow: hidden;
    background: var(--backdrop);
    font-family: "Lato", Arial, sans-serif;
  }
  .stage {
    position: relative; width: 1200px; height: 1023px;
  }
  .card {
    position: absolute; left: 250px; width: 700px; height: 400px;
    box-shadow: 0 6px 18px rgba(0,0,0,0.18);
  }
  .card--back {
    top: 80px; background: var(--navy);
    display: flex; align-items: center; justify-content: center;
  }
  .card--back .brand-name {
    color: var(--sky); font-weight: 900; font-size: 50px;
    letter-spacing: 1px; text-transform: uppercase;
  }
  .card--front {
    top: 540px; background: var(--paper);
  }
  .card--front .brand-name {
    position: absolute; left: 36px; top: 58px;
    color: var(--teal); font-weight: 900; font-size: 46px;
    letter-spacing: 1px; text-transform: uppercase;
  }
  .holder {
    position: absolute; right: 52px; top: 178px; text-align: center;
  }
  .holder__name {
    color: var(--azure); font-weight: 700; font-size: 25px;
    text-transform: uppercase; letter-spacing: 0.5px;
  }
  .holder__title {
    color: var(--ink); font-size: 19px; line-height: 1.1;
  }
  .contact {
    position: absolute; left: 36px; top: 248px;
    font-size: 17px; line-height: 21px; color: var(--ink);
  }
  .contact__address { margin-bottom: 6px; }
  .contact__label { color: var(--azure); }
  .contact__row { line-height: 23px; }
</style>
</head>
<body>
<main class="stage">
  <section class="card card--back" aria-label="Card back">
    <div class="brand-name">Velmora Sound House</div>
  </section>

  <section class="card card--front" aria-label="Card front">
    <div class="brand-name">Velmora Sound House</div>

    <div class="holder">
      <div class="holder__name">Dale Fornwick</div>
      <div class="holder__title">President</div>
    </div>

    <div class="contact">
      <div class="contact__address">418 Willow Bend Lane<br>Ashgrove Falls, NY 10599</div>
      <div class="contact__row"><span class="contact__label">phone:</span> +1 310.555.7182</div>
      <div class="contact__row"><span class="contact__label">email:</span> dale@velmorasoundhouse.com</div>
      <div class="contact__row"><span class="contact__label">url:</span> www.velmorasoundhouse.com</div>
    </div>
  </section>
</main>
</body>
</html>
```